Halvorsen Basin Holdings, LP Letter Head

We need an official company letter head design that is clean and mimics our company logo style. It will include our logo, address, phone, and website. We are an OIl and Gas mineral purchasing company, so hints of oil rigs or related design would be desirable.

Industry/Entity Type

Oil And Gas

Colors
ec1f27
f04a50
f59195
fbd4d5

Requirements
Must have
• Logo
• 7316 Marwick T. Ellsbury Parkway, Suite 418
• Dallas TX, 75391
• 214-763-1957
• www.halvorsenbasin.com
Nice to have
• Oil Rigs or OIl and gas related design

```html
<!DOCTYPE html>
<html lang="en">
<head>
<meta charset="utf-8">
<title>Halvorsen Basin Holdings, LP — Letterhead</title>
<link href="https://fonts.googleapis.com/css2?family=Open+Sans:wght@400;600&display=swap" rel="stylesheet">
<style>
  :root {
    --brand-red: #c4202a;
    --brand-red-bright: #ec1f27;
    --ink: #2a2a2a;
    --ink-soft: #444;
    --paper: #ffffff;
    --backdrop: #ececec;
    --watermark: #f1f1f1;
    --signature-tone: #e6e6e6;
  }
  html, body {
    margin: 0;
    width: 1200px;
    height: 794px;
    overflow: hidden;
    background: var(--backdrop);
    font-family: "Open Sans", Arial, sans-serif;
  }
  .letterhead {
    position: absolute;
    left: 330px;
    top: 15px;
    width: 540px;
    height: 764px;
    background: var(--paper);
    box-shadow: 0 2px 10px rgba(0,0,0,0.08);
    overflow: hidden;
  }
  .top-rule {
    position: absolute;
    left: 0; right: 0; top: 0;
    height: 3px;
    background: var(--brand-red);
  }
  .bottom-band {
    position: absolute;
    left: 0; right: 0; bottom: 0;
    height: 14px;
    background: var(--brand-red);
  }
  .brand {
    position: absolute;
    top: 74px;
    left: 0; right: 0;
    display: flex;
    justify-content: center;
    align-items: center;
    gap: 9px;
  }
  .brand-mark {
    width: 26px;
    height: 26px;
    background: var(--brand-red);
  }
  .brand-name {
    font-size: 17px;
    font-weight: 400;
    color: var(--brand-red);
    letter-spacing: 0.5px;
  }
  .letter-body {
    position: absolute;
    top: 190px;
    left: 72px;
    width: 396px;
    font-size: 8.4px;
    line-height: 1.55;
    color: var(--ink);
  }
  .letter-body p { margin: 0 0 11px; }
  .signature {
    position: absolute;
    top: 405px;
    left: 74px;
    width: 140px;
    height: 50px;
    background: var(--signature-tone);
    border-radius: 3px;
  }
  .watermark {
    position: absolute;
    left: 300px;
    top: 420px;
    width: 170px;
    height: 170px;
    border: 10px solid var(--watermark);
    box-sizing: border-box;
  }
  .contact {
    position: absolute;
    right: 38px;
    bottom: 36px;
    text-align: right;
    font-size: 8.6px;
    color: var(--ink);
    line-height: 1.75;
  }
  .contact-row {
    display: flex;
    justify-content: flex-end;
    align-items: center;
    gap: 4px;
  }
  .contact-row svg { width: 8px; height: 8px; fill: var(--brand-red-bright); }
  .contact-row .sep { width: 6px; }
</style>
</head>
<body>
  <main class="letterhead">
    <div class="top-rule"></div>

    <header class="brand">
      <div class="brand-mark"></div>
      <div class="brand-name">Halvorsen Basin Holdings, LP</div>
    </header>

    <section class="letter-body">
      <p>Thank you for your continued interest in our mineral and royalty acquisition program. This letter confirms receipt of your recent ownership records and outlines the next steps in our review. Our land team will evaluate title, production history and lease terms before preparing a formal offer for your consideration.</p>
      <p>We expect to complete the evaluation within fifteen business days. During this period, please keep any division orders, check stubs or lease copies close at hand, as our analysts may contact you to clarify acreage or decimal interest figures.</p>
      <p>Should you have questions at any time, our office is glad to help. We value a transparent process and look forward to building a lasting working relationship with you and your family.</p>
    </section>

    <div class="signature" role="img" aria-label="Handwritten signature of Erik Lindqvist"></div>

    <div class="watermark" aria-hidden="true"></div>

    <footer class="contact">
      <div class="contact-row">7316 Marwick T. Ellsbury Parkway, Suite 418, Dallas TX, 75391</div>
      <div class="contact-row">
        <svg viewBox="0 0 24 24" aria-hidden="true"><path d="M6.6 10.8a15 15 0 0 0 6.6 6.6l2.2-2.2c.3-.3.7-.4 1-.2 1.1.4 2.3.6 3.6.6.6 0 1 .4 1 1V20c0 .6-.4 1-1 1A17 17 0 0 1 3 4c0-.6.4-1 1-1h3.5c.6 0 1 .4 1 1 0 1.3.2 2.5.6 3.6.1.3 0 .7-.2 1z"/></svg>
        <span>214-763-1957</span>
        <span class="sep"></span>
        <svg viewBox="0 0 24 24" aria-hidden="true"><path d="M2 5h20v14H2zM3.5 6.5 12 13l8.5-6.5z"/></svg>
        <span>info@halvorsenbasin.com</span>
        <span class="sep"></span>
        <svg viewBox="0 0 24 24" aria-hidden="true"><circle cx="12" cy="12" r="10"/></svg>
        <span>www.halvorsenbasin.com</span>
      </div>
    </footer>

    <div class="bottom-band"></div>
  </main>
</body>
</html>
```